Buch-/eBook-Cover für einen Elternratgeber
Zielgruppe
Buch: Elternratgeber
Titel: Zahlen fühlen
Untertitel: Deinem Kind den richtigen Umgang beibringen
Wir sind der ULM Verlag und suchen ein passendes Cover für unseren neuen Elternratgeber. Mit diesem Buch möchten wir Eltern unterstützen, ihren Kindern einen guten und verantwortungsvollen Umgang mit Geld zu vermitteln.
Anforderungen an das Cover-Design:
Bitte keinen Comicstil
Das Buch richtet sich an Eltern (nicht kindlich oder verspielt gestalten)
Keine direkte Darstellung von Geld (z. B. keine Münzen, Geldscheine, Sparschweine usw.)
Ob mit oder ohne Personen auf dem Cover: sind wir offen
Farbwahl und Bildsprache: gerne seriös, ansprechend und modern
Wir sind gespannt auf kreative und professionelle Vorschläge!
E-Book E-Book"
Das Design darf nicht zu überladen sein.

```html
<!DOCTYPE html>
<html lang="de">
<head>
<meta charset="utf-8">
<title>Zahlen fühlen – ULM Verlag</title>
<link rel="stylesheet" href="https://fonts.googleapis.com/css2?family=Source+Serif+4:opsz,wght@8..60,700&family=Instrument+Sans:wght@400;500;600&display=swap">
<style>
  :root {
    --paper: #f9f1e5;
    --ink: #1f4357;
    --navy: #213a52;
    --slate: #56737f;
    --rust: #bd6a40;
    --skin: #efc7a4;
    --table: #f1dfc6;
  }
  html, body {
    margin: 0;
    padding: 0;
    overflow: hidden;
    background: var(--paper);
  }
  .cover {
    position: relative;
    width: 800px;
    height: 1200px;
    overflow: hidden;
    background: var(--paper);
    color: var(--ink);
  }
  .publisher {
    position: absolute;
    left: 57px;
    top: 44px;
    margin: 0;
    font-family: "Instrument Sans", sans-serif;
    line-height: 1;
    color: var(--ink);
  }
  .publisher-name {
    display: block;
    font-size: 32px;
    font-weight: 600;
    letter-spacing: 0.5px;
  }
  .publisher-label {
    display: block;
    margin-top: 2px;
    font-size: 27px;
    font-weight: 500;
    letter-spacing: 1px;
  }
  .title {
    position: absolute;
    left: 0;
    right: 0;
    top: 134px;
    margin: 0;
    text-align: center;
    font-family: "Source Serif 4", serif;
    font-weight: 700;
    font-size: 140px;
    line-height: 119px;
    letter-spacing: -1px;
    color: var(--ink);
  }
  .title span { display: block; }
  .subtitle {
    position: absolute;
    left: 0;
    right: 0;
    top: 398px;
    margin: 0;
    text-align: center;
    font-family: "Instrument Sans", sans-serif;
    font-weight: 400;
    font-size: 37px;
    line-height: 47px;
    color: var(--ink);
  }
  .table {
    position: absolute;
    left: 0;
    top: 1038px;
    width: 800px;
    height: 162px;
    background: var(--table);
  }
  .illustration {
    position: absolute;
    left: 0;
    top: 505px;
    width: 800px;
    height: 600px;
    background:
      radial-gradient(ellipse 150px 190px at 330px 470px, rgba(86,115,127,0.95) 0%, rgba(86,115,127,0.85) 55%, rgba(86,115,127,0) 100%),
      radial-gradient(ellipse 230px 330px at 190px 330px, rgba(33,58,82,0.95) 0%, rgba(33,58,82,0.85) 60%, rgba(33,58,82,0) 100%),
      radial-gradient(ellipse 210px 300px at 590px 380px, rgba(189,106,64,0.95) 0%, rgba(189,106,64,0.8) 60%, rgba(189,106,64,0) 100%),
      radial-gradient(ellipse 120px 130px at 530px 200px, rgba(239,199,164,0.9) 0%, rgba(239,199,164,0) 100%);
  }
</style>
</head>
<body>
  <main class="cover">
    <p class="publisher">
      <span class="publisher-name">ULM</span>
      <span class="publisher-label">VERLAG</span>
    </p>
    <h1 class="title"><span>Zahlen</span><span>fühlen</span></h1>
    <p class="subtitle">Deinem Kind den richtigen<br>Umgang beibringen</p>
    <div class="table"></div>
    <div class="illustration" role="img" aria-label="Illustration: Eine Mutter im dunkelblauen Pullover und ihr Sohn im rostroten Pullover sitzen am Tisch und lesen gemeinsam in einem blaugrauen Buch mit Euro-Zeichen; die Mutter erklärt mit erhobenem Finger."></div>
  </main>
</body>
</html>
```